Cover-Design für Buch über Corona-Pandemie
Zielgruppe
Ich bin ein junger Arzt und schreibe ein Buch über die Corona Pandemie. Zielgruppe sind alle Menschen, die sich kritisch aber seriös mit der Thematik befassen. Ich werde das Buch selbst veröffentlichen über Buchwelt oder ähnliche Portale.
Aufgabenstellung
Sehr geehrte Designer,
ich hätte gern das Buchcover mit Vorderseite und Hinterseite. Die beiden Textvorlagen befinden sich in der hochgeladenen Datei. Seite 1 ist die Vorderseite, Seite 2 die Hinterseite des Buchcovers.
Sie können sich grob an dem Buchcover 'Fieber Irrtum' von Wendorf orientieren. Also ein sehr großer Titel in rot, schlicht gestaltet, unter dem Titel der Untertitel in schwarz, so wie in der angehängten Datei. Der Titel sollte ebenfalls auf zwei Zeilen in großer Schrift aufgeteilt sein wie von Wendorf. Der Autorenname sollte ganz unten auf der Coverseite zentral seinTitel, Untertitel und Autorenname sollten ca. 60% der Länge des Buchcovers ausmachen. Die Ähnlichkeit zum Wendorf Buch sollte wegen dem Urheberrecht nicht zu groß ist, aber da kennen Sie sich sicher besser aus und können sicher entsprechende Modifikationen machen. So kann man ja z.B Weinrot verwenden oder andere Formatierungen.
Darunter hätte ich gerne ein Gehirn, mit Injektionsspritzen, die in das Gehirn stechen und wie ein Kranz um das Gehirn gereiht sind Daneben sollte ein CoronaVirus sein, dessen Hülle dem Gehirn mit den Spritzen sehr ähnlich sieht. Beides in Schwarz-Weiß. Als grobe Orientierungshilfe habe ich selbst ein Gehirn mit den Spritzen in der Datei entworfen, damit Sie eine ungefähre Idee von der Optik haben.
Wenn Sie echte Abbildungen von Gehirn und Spritzen finden und sie in der Bildbearbeitung so nach meiner Vorlage gestalten können, wäre es am Schönsten. Sonst können sie einfach auch Symbole oder Comics wie ich verwenden, solange das Gehirn und das Virus optisch zusammenpassen und den gleichen Stil haben.
Sonst i Stil klare Linien, Minimalistisch.
Auf der Hinterseite des Cover sollte wie in der angehängten Datei das Zitat rot sein, der Text schwarz, sonst habe ich keine weiteren Wünsche.
Vielen Dank!
UPDATE: Zusätzliche hätte ich gerne ein Bild von mir und den Text über den Autor auf der Hinter..

```html
<!DOCTYPE html>
<html lang="de">
<head>
<meta charset="utf-8">
<title>Pandemie Irrsinn? – Buchumschlag</title>
<link rel="stylesheet" href="https://fonts.googleapis.com/css2?family=Oswald:wght@700&family=Jost:wght@400;500;600&family=Roboto+Condensed:wght@700&display=swap">
<style>
  :root {
    --page-bg: #e9e9ea;
    --cover-bg: #ffffff;
    --cover-edge: #d6d6d8;
    --title-wine: #9b1c2c;
    --quote-red: #c8262e;
    --ink: #161616;
    --art-red: #d8434a;
    --art-grey: #b7b9bd;
    --photo-grey: #c9cacc;
  }
  * { box-sizing: border-box; margin: 0; padding: 0; }
  html, body { width: 1200px; height: 675px; overflow: hidden; }
  body { background: var(--page-bg); position: relative; }

  .cover {
    position: absolute;
    top: 95px;
    width: 338px;
    height: 477px;
    background: linear-gradient(180deg, var(--cover-bg) 0%, #f4f4f5 100%);
    box-shadow: 0 0 0 1px var(--cover-edge), 0 6px 14px rgba(0,0,0,0.12);
    overflow: hidden;
  }
  .cover--back { left: 212px; }
  .cover--front { left: 656px; }

  /* Back cover */
  .back-quote {
    position: absolute;
    top: 54px; left: 48px; right: 48px;
    font-family: "Jost", sans-serif;
    font-weight: 500;
    font-size: 14.6px;
    line-height: 17px;
    color: var(--quote-red);
    text-align: center;
  }
  .back-blurb {
    position: absolute;
    top: 159px; left: 39px; width: 260px;
    font-family: "Jost", sans-serif;
    font-weight: 500;
    font-size: 8.7px;
    line-height: 10.3px;
    color: var(--ink);
    text-align: justify;
  }
  .back-blurb p + p { margin-top: 10px; }

  .author-photo {
    position: absolute;
    top: 339px; left: 39px;
    width: 82px; height: 82px;
    background: linear-gradient(180deg, var(--photo-grey) 0%, #b9bcc2 100%);
  }
  .author-bio {
    position: absolute;
    top: 360px; left: 128px; width: 171px;
    font-family: "Jost", sans-serif;
    color: var(--ink);
  }
  .author-bio h2 {
    font-size: 8.2px;
    font-weight: 600;
    margin-bottom: 9px;
  }
  .author-bio p {
    font-size: 7.3px;
    font-weight: 500;
    line-height: 9px;
    text-align: justify;
    hyphens: auto;
  }

  /* Front cover */
  .front-title { position: absolute; top: 0; left: 0; width: 338px; height: 150px; }
  .front-title text { font-family: "Oswald", sans-serif; font-weight: 700; fill: var(--title-wine); }
  .front-subtitle {
    position: absolute;
    top: 150px; left: 8px; right: 8px;
    font-family: "Roboto Condensed", sans-serif;
    font-weight: 700;
    font-size: 13px;
    line-height: 17px;
    color: var(--ink);
    text-align: center;
  }
  .front-art {
    position: absolute;
    top: 202px; left: 39px;
    width: 211px; height: 219px;
    border-radius: 50%;
    background: radial-gradient(circle at 62% 55%, var(--art-red) 0%, var(--art-red) 36%, rgba(216,67,74,0.3) 54%, rgba(183,185,189,0.3) 66%, rgba(255,255,255,0) 72%);
  }
  .front-author {
    position: absolute;
    top: 435px; left: 0; right: 0;
    font-family: "Roboto Condensed", sans-serif;
    font-weight: 700;
    font-size: 11px;
    color: var(--ink);
    text-align: center;
  }
</style>
</head>
<body>

<section class="cover cover--back" aria-label="Buchrückseite">
  <blockquote class="back-quote">„Die bewusste und zielgerichtete Manipulation der Verhaltensweisen und Einstellungen der Massen ist ein wesentlicher Bestandteil westlicher Demokratien.“</blockquote>

  <div class="back-blurb">
    <p>Schon der Begründer der Public Relations und Neffe von Siegfried Brandt, Edwin Barlow, erkannte 1928 die zentrale Rolle des Meinungsmanagements, das aktueller denn je ist.</p>
    <p>Die Pandemie reißt gewaltige Gräben innerhalb unserer Gesellschaft auf. Emotionalisierung, Moralisierung und Manipulation vergiften die inhaltliche Diskussion von Mensch zu Mensch, die Basis von Wissenschaft, Demokratie und Beziehungen. Dieser verzerrte Diskurs verlegt Lösungswege aus der Pandemie.</p>
    <p>Das Buch zeigt viele etablierte Manipulationstechniken, die seit Jahrzehnten von Politik, Medien und Wirtschaft angewendet werden, um die öffentliche Meinung zu beeinflussen. Außerdem beleuchtet es logische Fehlschlüsse, die viele Argumentationen ungültig machen.</p>
  </div>

  <div class="author-photo" role="img" aria-label="Porträtfoto des Autors"></div>
  <div class="author-bio">
    <h2>Über den Autor</h2>
    <p>Jonas Wieland, geboren 1992 in der Ober&shy;steiermark, arbeitet als Arzt in Ausbildung zum Allgemeinmediziner in einer Wiener Klinik. Er erlebt als junger Mediziner die Corona&shy;pandemie an vorderster Front.</p>
  </div>
</section>

<section class="cover cover--front" aria-label="Buchvorderseite">
  <svg class="front-title" viewBox="0 0 338 150" role="heading" aria-level="1" aria-label="Pandemie Irrsinn?">
    <text x="10" y="84" font-size="84" textLength="318" lengthAdjust="spacingAndGlyphs">PANDEMIE</text>
    <text x="10" y="143" font-size="58" textLength="318" lengthAdjust="spacingAndGlyphs">IRRSINN?</text>
  </svg>

  <p class="front-subtitle">Wie Meinungsmanagement und logische Fehlschlüsse<br>unser Denken vergiften.</p>

  <div class="front-art" role="img" aria-label="Illustration: rotes Gehirn, zur Hälfte als Virus, mit einem Kranz aus Injektionsspritzen"></div>

  <p class="front-author">Dr. med. univ. Jonas Wieland</p>
</section>

</body>
</html>
```